Vendrick Legal PLLC updated letterhead for solo law practice - legal/professional services

I need a new letterhead design on a word document for my solo law practice. I have attached my current letterhead. Here is my company info:

Dorian Vendrick
Vendrick Legal PLLC
2718 Brambleton, Suite 430
Dallas, Texas 75291
Phone: 214 555 0187
Email: dorian@vendrick-legal.example
Website: www.vendrick-legal.example

Preferably I'd like the logo on top followed by my name and email (in the header)

At the bottom (footer) i'd like the rest of the information.

I am fine using a color for the line in between "Vendrick" and "Legal" in the "Vendrick Legal" logo. Or a different font.

Industry/Entity Type

Legal

Font styles to use
Serif

Colors

Designer to choose only greyscale colors for use in the design.

Requirements
Must have
• The "Vendrick Legal" logo with the line in between "Vendrick" and "Legal" but I am open to ideas on structure and color schemes.
Nice to have
• Logo on top with new color scheme, along with my name and email.
• Address, phone number, web address on bottom.

```html
<!DOCTYPE html>
<html lang="en">
<head>
<meta charset="utf-8">
<title>Vendrick Legal PLLC — Letterhead</title>
<link rel="stylesheet" href="https://fonts.googleapis.com/css2?family=Cormorant+Garamond:wght@500&family=Tinos:wght@400;700&display=swap">
<style>
  :root {
    --backdrop: #1a1a1a;
    --paper: #ffffff;
    --accent: #7d7d7d;
    --accent-deep: #555555;
    --charcoal: #333333;
    --ink: #111111;
  }
  * { margin: 0; padding: 0; box-sizing: border-box; }
  html, body { width: 1200px; height: 1000px; overflow: hidden; background: var(--backdrop); }
  .letterhead {
    position: absolute; left: 265px; top: 26px; width: 671px; height: 949px;
    background: var(--paper); color: var(--ink);
    font-family: "Tinos", "Times New Roman", serif; font-size: 13.5px; line-height: 16.3px;
    overflow: hidden;
  }
  .frame-shapes { position: absolute; inset: 0; width: 671px; height: 949px; }
  .logo {
    position: absolute; left: 63px; top: 57px;
    display: flex; align-items: center; gap: 9px;
    font-family: "Cormorant Garamond", "Times New Roman", serif; font-weight: 500;
    font-size: 25px; line-height: 30px; letter-spacing: 1.2px; color: var(--ink); white-space: nowrap;
  }
  .logo-divider { display: block; width: 1.5px; height: 37px; background: var(--ink); }
  .header-contact {
    position: absolute; left: 385px; top: 53px; color: var(--paper);
    font-size: 14px; line-height: 18px; white-space: nowrap;
  }
  .header-contact strong { font-weight: 700; }
  .header-contact .dot { margin: 0 4px; }
  .header-email { display: flex; align-items: center; gap: 7px; }
  .recipient { position: absolute; left: 63px; top: 154px; }
  .recipient strong { font-weight: 700; }
  .recipient-details { position: absolute; left: 63px; top: 217px; }
  .recipient-details .row { display: flex; }
  .recipient-details .key { width: 19px; }
  .letter-date { position: absolute; right: 49px; top: 249px; }
  .letter-body { position: absolute; left: 63px; top: 300px; width: 566px; }
  .letter-body p { margin-bottom: 16.3px; }
  .signature-mark {
    position: absolute; left: 66px; top: 694px; width: 61px; height: 47px;
    background: linear-gradient(135deg, #e6e6e6, #f5f5f5); border-radius: 4px;
  }
  .signatory { position: absolute; left: 63px; top: 749px; }
  .signatory strong { font-weight: 700; }
  .footer-item { position: absolute; display: flex; align-items: center; gap: 10px; top: 893px; }
  .footer-icon {
    width: 26px; height: 26px; border-radius: 3px; background: var(--accent-deep);
    display: flex; align-items: center; justify-content: center; flex: none;
  }
  .footer-text { font-size: 13px; line-height: 16px; white-space: nowrap; }
  .footer-address { left: 63px; }
  .footer-phone { left: 288px; }
  .footer-web { left: 463px; }
  .footer-web .footer-text { font-size: 12px; letter-spacing: -0.1px; }
</style>
</head>
<body>
<div class="letterhead">
  <svg class="frame-shapes" viewBox="0 0 671 949" aria-hidden="true">
    <polygon points="0,0 20,0 20,474 0,491" fill="var(--accent)"/>
    <polygon points="0,517 20,501 20,581 0,597" fill="var(--charcoal)"/>
    <polygon points="369,42 671,42 671,109 330,109" fill="var(--accent)"/>
    <polygon points="651,703 671,686 671,765 651,782" fill="var(--accent-deep)"/>
    <polygon points="651,808 671,791 671,949 651,949" fill="var(--charcoal)"/>
  </svg>

  <div class="logo">
    <span>VENDRICK</span>
    <span class="logo-divider" aria-hidden="true"></span>
    <span>LEGAL</span>
  </div>

  <div class="header-contact">
    <div><strong>Dorian Vendrick</strong><span class="dot">•</span>Vendrick Legal PLLC</div>
    <div class="header-email">
      <svg width="13" height="9" viewBox="0 0 13 9" aria-hidden="true"><rect width="13" height="9" rx="1" fill="#fff"/><path d="M0.5 0.8 L6.5 5 L12.5 0.8" fill="none" stroke="var(--accent)" stroke-width="1.2"/></svg>
      <span>dorian@vendrick-legal.example</span>
    </div>
  </div>

  <div class="recipient">
    <div>To</div>
    <div><strong>Martin Hale</strong></div>
    <div>Chief Director</div>
  </div>

  <div class="recipient-details">
    <div class="row"><span class="key">A</span><span>: Harbor Lane, New York, USA</span></div>
    <div class="row"><span class="key">W</span><span>: www.martinhale.example</span></div>
    <div class="row"><span class="key">P</span><span>: (012) 555 0143</span></div>
  </div>

  <div class="letter-date">Date : 21 November, 2019</div>

  <div class="letter-body">
    <p>Lorem ipsum dolor sit amet, consectetur adipiscing elit. Curabitur euismod, quam nec sollicitudin faucibus, tellus ante varius erat, sit amet varius velit sapien sit amet lorem. Aliquam accumsan libero sed pretium congue. Maecenas ac vehicula lacus, a pretium purus. Sed consequat aliquet lacus vitae bibendum. Aliquam pretium rutrum faucibus. Aenean mi nibh, blandit in enim ac, gravida finibus lectus. Vestibulum ut justo iaculis, semper ante at, iaculis massa. Etiam volutpat finibus sagittis. Integer accumsan velit eros, a maximus ligula varius id. Integer vel magna erat.</p>
    <p>Nam a elementum ante, eget efficitur urna. Donec finibus aliquet aliquet. Nullam ultrices accumsan ullamcorper. Fusce quis interdum turpis, at dictum mi. Nulla scelerisque tortor arcu, eget sagittis tellus tempus in. Integer nec condimentum quam. Aenean molestie dictum nibh ac semper. Aliquam erat volutpat.</p>
    <p>Donec ut neque scelerisque, vulputate ipsum sed, rhoncus enim. Nam at urna justo. Morbi vel dignissim justo. Praesent sollicitudin urna vitae massa commodo, eget vulputate ligula tempor. Vestibulum convallis iaculis turpis non semper. Donec ornare ut lacus eget euismod. Nam pretium rutrum sem quis accumsan. Cras in elit id eros efficitur porta nec eget diam. Sed fringilla consectetur nulla, rutrum aliquet lorem dictum non. Nulla id ultrices lorem. Integer id finibus eros. Maecenas gravida eros eget nisl tincidunt gravida. In sed erat dignissim, aliquet urna eget, scelerisque libero.</p>
    <p>Ut laoreet nisi eu nunc vulputate vestibulum. Nunc eu congue odio. Phasellus lacinia eu sem eu elementum. Suspendisse at arcu elit. Vivamus ultricies eleifend erat eget pretium. Morbi tristique urna at arcu volutpat, in tincidunt neque ullamcorper.</p>
  </div>

  <div class="signature-mark" role="img" aria-label="Handwritten signature of the sender"></div>

  <div class="signatory">
    <div><strong>Evan Marlow</strong></div>
    <div>Manager</div>
  </div>

  <div class="footer-item footer-address">
    <span class="footer-icon">
      <svg width="14" height="16" viewBox="0 0 14 16" aria-hidden="true"><path d="M7 15 C3 10 2 8 2 6 A5 5 0 0 1 12 6 C12 8 11 10 7 15 Z" fill="none" stroke="#fff" stroke-width="1.2"/><circle cx="7" cy="6" r="1.8" fill="none" stroke="#fff" stroke-width="1.2"/></svg>
    </span>
    <span class="footer-text">2718 Brambleton, Suite 430<br>Dallas, Texas 75291</span>
  </div>

  <div class="footer-item footer-phone">
    <span class="footer-icon">
      <svg width="15" height="15" viewBox="0 0 15 15" aria-hidden="true"><path d="M3 1.5 L5.5 1.5 L6.5 4.5 L5 5.8 C5.8 7.6 7.4 9.2 9.2 10 L10.5 8.5 L13.5 9.5 L13.5 12 C13.5 12.8 12.8 13.5 12 13.5 C6.2 13.2 1.8 8.8 1.5 3 C1.5 2.2 2.2 1.5 3 1.5 Z" fill="none" stroke="#fff" stroke-width="1.1" stroke-linejoin="round"/></svg>
    </span>
    <span class="footer-text">( 214 ) 555 0187</span>
  </div>

  <div class="footer-item footer-web">
    <span class="footer-icon">
      <svg width="15" height="15" viewBox="0 0 15 15" aria-hidden="true"><g fill="none" stroke="#fff" stroke-width="1"><circle cx="7.5" cy="7.5" r="6"/><ellipse cx="7.5" cy="7.5" rx="2.6" ry="6"/><line x1="1.5" y1="7.5" x2="13.5" y2="7.5"/><line x1="2.5" y1="4.5" x2="12.5" y2="4.5"/><line x1="2.5" y1="10.5" x2="12.5" y2="10.5"/></g></svg>
    </span>
    <span class="footer-text">www.vendrick-legal.example</span>
  </div>
</div>
</body>
</html>
```